New automotive search style homepage

Looking for someone that can create a new homepage layout for my company. What we currently have is a little plain above the fold. We are an automotive technology company, where we take over the negotiation for customers, and perhaps we can have a design that appeals to that idea more. The current chat container is our only way to search currently, but would love to have a hybrid chat and manual search container, with the manual fields being make and model. This shouldn't have a toggle, but a seamless split view housing both features. You can see current design of our site at motorlane.net

Target Market(s)

Car buyers

Industry/Entity Type

Automotive

Number of Pages Required

1 page

Colors
0054AA
0677BA
7BADD7
CADEEF
E8F1F8

Requirements
Must have
• Above the fold is the most important

```html
<!DOCTYPE html>
<html lang="en">
<head>
<meta charset="utf-8">
<title>MotorLane — Find Your Next Car</title>
<link href="https://fonts.googleapis.com/css2?family=Lexend+Exa:wght@300;400;500;600;700&family=Montserrat:wght@400;500;600;700&display=swap" rel="stylesheet">
<style>
:root{
  --blue:#0b7bff;
  --blue-deep:#0054aa;
  --blue-mid:#0677ba;
  --blue-soft:#7badd7;
  --blue-pale:#cadeef;
  --blue-mist:#e8f1f8;
  --yellow:#ffc21a;
  --ink:#1f2633;
  --muted:#5a6372;
  --navy:#0a1226;
  --panel:#0f1a33;
  --panel-line:#1e2c4f;
  --green:#27d17f;
  --white:#fff;
  --head:"Lexend Exa",sans-serif;
  --body:"Montserrat",sans-serif;
}
*{box-sizing:border-box;margin:0;padding:0}
html,body{width:1200px;height:3333px;overflow:hidden}
body{position:relative;font-family:var(--body);color:var(--ink);background:#fff}
.sec{position:absolute;left:0;width:1200px;overflow:hidden}
.abs{position:absolute}
.h-title{font-family:var(--head);font-weight:500;font-size:31px;text-align:center;width:100%;letter-spacing:1px}
.h-sub{font-family:var(--head);font-size:11px;text-align:center;width:100%;color:var(--muted);letter-spacing:.3px}
.btn{position:absolute;display:flex;align-items:center;justify-content:center;gap:8px;font-family:var(--head);font-size:11px;border-radius:3px}
.btn-solid{background:var(--blue);color:#fff}
.btn-line{border:1.5px solid var(--blue);color:var(--blue);background:#fff}
.btn-ghost{border:1.5px solid #fff;color:#fff}
.logo{font-family:var(--head);font-weight:700;color:#fff;display:flex;align-items:center;gap:8px}
.logo-dot{width:12px;height:12px;border-radius:50%;background:#fff}

/* hero */
.hero{top:0;height:347px;background:linear-gradient(180deg,#4f7fb4 0%,#7ea3c9 45%,#6b8bb0 75%,#4e6d94 100%)}
.hero-photo{position:absolute;left:500px;top:150px;width:700px;height:197px;background:radial-gradient(ellipse at 62% 60%,#1f5fd6 0%,#1848a8 28%,rgba(40,80,150,.0) 60%)}
.nav{position:absolute;top:20px;left:118px;right:117px;height:22px;display:flex;align-items:center}
.nav .logo{font-size:17px}
.nav-links{position:absolute;left:305px;display:flex;gap:18px;font-family:var(--head);font-size:10px;color:#fff}
.nav-btn{position:absolute;top:0;height:20px;width:100px;font-family:var(--head);font-size:10px;display:flex;align-items:center;justify-content:center;border-radius:2px}
.hero h1{position:absolute;left:111px;top:110px;font-family:var(--head);font-weight:500;color:#fff;font-size:26px;line-height:28px;letter-spacing:.5px}
.hero h1 strong{font-size:36px;font-weight:700}
.hero-lead{position:absolute;left:117px;top:212px;width:400px;font-family:var(--head);font-size:12px;line-height:14px;color:#fff}
.stats{position:absolute;top:311px;left:0;width:1200px;font-family:var(--head);color:#fff}
.stat{position:absolute;display:flex;align-items:baseline;gap:8px;font-size:13px}
.stat b{font-size:22px;font-weight:700}

/* find */
.find{top:347px;height:146px;background:var(--blue)}
.find-photo{position:absolute;left:55px;top:18px;width:330px;height:128px;border-radius:40% 45% 10% 10%;background:linear-gradient(180deg,#2d5db8,#123a86 60%,#0d1e3f)}
.find h2{position:absolute;left:362px;top:12px;font-family:var(--head);font-weight:400;font-size:40px;color:#fff;letter-spacing:3px}
.select{position:absolute;top:69px;height:22px;background:#fff;border-radius:2px;font-family:var(--head);font-size:10px;color:#444;display:flex;align-items:center;justify-content:space-between;padding:0 10px 0 14px}
.find-quote{position:absolute;left:508px;top:109px;font-family:var(--head);font-size:10px;color:#fff}
.find-go{position:absolute;left:826px;top:103px;width:211px;height:25px;background:var(--yellow);border-radius:2px;font-family:var(--head);font-size:11px;color:#111;display:flex;align-items:center;justify-content:center;gap:10px}

/* how */
.how{top:493px;height:331px;background:#fff}
.step{position:absolute;top:140px;width:200px}
.step-num{position:absolute;top:-4px;font-family:var(--head);font-weight:600;font-size:28px;color:var(--blue)}
.step h3{position:absolute;top:48px;font-family:var(--head);font-weight:500;font-size:11.5px;line-height:13px;width:200px}
.step p{position:absolute;top:78px;font-family:var(--head);font-size:8.5px;line-height:10px;color:var(--muted);width:170px}
.step-div{position:absolute;top:138px;width:24px;height:106px}

/* deals */
.deals{top:824px;height:433px;background:linear-gradient(180deg,#1e78c8 0%,#4da3e0 30%,#8cc6ee 62%,#c7dbe6 84%,#8d8a63 94%,#6c6a45 100%)}
.deals .h-title,.deals .h-sub{color:#fff}
.deal{position:absolute;top:94px;height:225px;background:#fff;border-radius:3px;padding:0 20px}
.deal-photo{position:absolute;left:14px;right:14px;top:12px;height:70px;border-radius:4px;background:radial-gradient(ellipse at 50% 60%,#3a3d44 0%,#6a6e76 45%,#f2f3f5 75%)}
.heart{position:absolute;right:12px;top:6px;width:26px;height:18px;border-radius:9px;background:var(--blue);display:flex;align-items:center;justify-content:center}
.deal h4{position:absolute;left:20px;top:92px;font-family:var(--head);font-weight:500;font-size:10.5px;line-height:11px;width:170px}
.deal .price{position:absolute;left:20px;top:123px;font-family:var(--head);font-weight:700;font-size:15px;color:var(--blue)}
.deal .miles{position:absolute;right:20px;top:127px;font-family:var(--head);font-size:8px;display:flex;gap:4px;align-items:center}
.deal .est{position:absolute;left:20px;top:143px;font-size:7px;font-family:var(--head)}
.deal .dom{position:absolute;left:27px;top:162px;font-size:7.5px;font-family:var(--head)}
.deal .color{position:absolute;left:24px;top:180px;font-size:7.5px;font-family:var(--head);display:flex;align-items:center;gap:8px}
.deal .color i{width:9px;height:9px;border-radius:50%;background:#111;display:block}
.deal .loc{position:absolute;left:24px;top:202px;font-size:7px;font-family:var(--head);display:flex;align-items:center;gap:8px}
.round{position:absolute;width:32px;height:18px;border-radius:9px;background:#fff;display:flex;align-items:center;justify-content:center}
.deals-car{position:absolute;left:540px;top:360px;width:280px;height:60px;border-radius:45% 50% 8% 8%;background:linear-gradient(180deg,#d7dbe0,#8f969f)}

/* compare */
.compare{top:1257px;height:805px;background:linear-gradient(180deg,#fff 0,#fff 182px,#0c1a3e 182px,#0a1226 100%)}
.col-old,.col-new{position:absolute;top:75px;height:181px;padding:18px 0 0 44px}
.col-old{left:163px;width:416px;background:#f1f2f4}
.col-new{left:579px;width:512px;background:var(--blue);color:#fff;padding-left:23px}
.col-old h3,.col-new h3{font-family:var(--head);font-weight:500;font-size:16px;margin-bottom:10px}
.col-old li,.col-new li{list-style:none;font-family:var(--head);font-size:10.5px;line-height:19.7px}
.col-old li::before,.col-new li::before{content:"›";margin-right:10px}
.compare-car{position:absolute;left:931px;top:178px;width:240px;height:84px;border-radius:40% 50% 10% 10%;background:linear-gradient(180deg,#3566c4,#163a80 65%,#0b1834)}
.powered{position:absolute;top:282px;width:100%;text-align:center;font-family:var(--head);font-weight:600;font-size:30px;line-height:33px;color:#fff;letter-spacing:1.5px}

/* dashboard */
.dash{position:absolute;left:101px;top:370px;width:998px;height:390px;color:#dfe6f5;font-family:var(--body)}
.side{position:absolute;left:0;top:0;width:132px;height:390px;border-right:1px solid var(--panel-line)}
.side .brand{position:absolute;left:10px;top:14px;font-family:var(--head);font-size:10px;font-weight:600;display:flex;gap:6px;align-items:center}
.side .brand i{width:12px;height:12px;border-radius:50%;background:var(--blue);display:block}
.side ul{position:absolute;top:44px;left:0;width:132px;list-style:none}
.side li{height:21px;font-size:8px;display:flex;align-items:center;gap:9px;padding-left:14px;color:#b9c4dc}
.side li i{width:8px;height:8px;border:1px solid #8fa0c4;border-radius:2px;display:block}
.side li.on{background:#13254b;border-right:2px solid var(--blue);color:#fff}
.side .badge{margin-left:auto;margin-right:10px;background:var(--blue);color:#fff;font-size:6px;padding:1px 5px;border-radius:5px}
.help{position:absolute;left:8px;top:322px;width:112px;height:44px;background:#111d3a;border-radius:4px;font-size:6.5px;padding:6px 0 0 28px}
.help b{display:block;font-size:7px;color:#fff}
.help span{position:absolute;left:12px;right:12px;bottom:6px;height:10px;background:var(--blue);border-radius:2px;text-align:center;font-size:6px;line-height:10px;color:#fff}
.dash-head{position:absolute;left:167px;top:8px}
.dash-head b{font-family:var(--head);font-size:11px;font-weight:600;color:#fff}
.dash-head p{font-size:7px;color:#9aa8c6;margin-top:2px}
.pill{position:absolute;top:12px;height:22px;border:1px solid var(--panel-line);background:#0e1831;border-radius:3px;font-size:7px;padding:4px 10px;color:#cfd8ea}
.card{position:absolute;top:43px;height:140px;background:var(--panel);border:1px solid var(--panel-line);border-radius:5px;padding:8px 10px}
.card .lbl{font-size:6.5px;font-weight:700;letter-spacing:.4px;color:#c3cde2}
.card .link{position:absolute;left:22px;right:14px;bottom:8px;font-size:6.5px;color:#4f9bff;display:flex;justify-content:space-between}
.card .note{position:absolute;left:0;right:0;text-align:center;font-size:6.5px;line-height:8px;color:#aebadb}
.big{font-family:var(--head);font-weight:600;color:#fff}
.insights{position:absolute;left:164px;top:193px;width:833px;height:148px;background:var(--panel);border:1px solid var(--panel-line);border-radius:5px}
.insights .lbl{position:absolute;font-size:6.5px;font-weight:700;color:#c3cde2;letter-spacing:.4px}
.tabs{position:absolute;right:16px;top:8px;display:flex;gap:4px}
.tabs span{font-size:6px;width:32px;height:12px;text-align:center;line-height:12px;border-radius:3px;background:#14203e;color:#aab6d2}
.tabs span.on{background:var(--blue);color:#fff}
.ins-col{position:absolute;top:28px;height:112px;border-right:1px solid var(--panel-line)}
.row{display:flex;align-items:center;font-size:6.5px;height:13.5px;color:#c7d1e6}
.row .bar{height:3px;border-radius:2px;margin:0 8px}
.ins-link{position:absolute;bottom:4px;font-size:6.5px;color:#4f9bff}
.dash-foot{position:absolute;left:164px;top:347px;width:833px;height:35px;border:1px solid #1f4aa8;border-radius:5px;background:#0d1838;font-size:7px;color:#aebadb}

/* popular */
.popular{top:2062px;height:227px;background:#fff}
.tile{position:absolute;top:99px;width:145px;height:102px;background:linear-gradient(180deg,#1e7dff,#0a64e3);color:#fff;font-family:var(--head);font-size:11.5px;font-weight:500;text-align:center}
.tile .ph{position:absolute;left:28px;right:28px;top:30px;height:30px;border-radius:40% 45% 12% 12%;background:linear-gradient(180deg,#5d6878,#1d2430)}
.tile span{position:absolute;left:0;right:0;top:74px}

/* testimonials */
.reviews{top:2289px;height:239px;background:#fff}
.review{position:absolute;top:84px;width:289px;height:86px;border:1px solid #e4e6ea;text-align:center;font-family:var(--head)}
.review .stars{margin-top:12px;color:var(--yellow);font-size:8px;letter-spacing:2px}
.review q{display:block;margin-top:6px;font-size:13px;line-height:13px;color:#333;padding:0 20px}
.review cite{display:block;font-style:normal;margin-top:5px;font-size:9px;color:var(--blue)}
.arrow-c{position:absolute;width:28px;height:18px;border-radius:9px;border:1px solid #d3d8e0;background:#eef1f5;display:flex;align-items:center;justify-content:center}

/* faq */
.faq{top:2528px;height:317px;background:linear-gradient(180deg,#eef3fb,#e3ebf6)}
.faq-word{position:absolute;left:420px;top:-30px;font-family:var(--head);font-size:128px;font-weight:500;color:#d6e1f6;white-space:nowrap;letter-spacing:4px}
.faq h2{position:absolute;left:134px;top:42px;font-family:var(--head);font-weight:500;font-size:28px;line-height:32px;color:#222}
.faq-photo{position:absolute;left:0;top:148px;width:440px;height:165px;border-radius:0 45% 8% 0;background:linear-gradient(180deg,#4e82b8,#1e4f84 60%,#16243d)}
.q{position:absolute;left:540px;width:470px;height:26px;border-bottom:1px solid #c8d3e4;font-family:var(--head);font-size:12px;color:#222;display:flex;align-items:center;justify-content:space-between}
.q i{width:28px;height:18px;border-radius:9px;background:var(--blue);color:#fff;font-style:normal;font-size:13px;display:flex;align-items:center;justify-content:center}

/* cta + footer */
.cta{top:2845px;height:488px;background:linear-gradient(180deg,#2f6fb5 0%,#5d95cd 25%,#a9c6dd 45%,#7b8ea4 56%,#505c6d 66%,#3d4756 80%,#2d3542 100%)}
.cta h2{position:absolute;top:38px;width:100%;text-align:center;font-family:var(--head);font-weight:600;font-size:31px;color:#fff;letter-spacing:1.5px}
.cta p{position:absolute;top:92px;width:100%;text-align:center;font-family:var(--head);font-size:11.5px;line-height:14px;color:#fff}
.cta-car{position:absolute;left:420px;top:216px;width:360px;height:80px;border-radius:40% 50% 10% 10%;background:linear-gradient(180deg,#6b7888,#2e3744)}
.foot-logo{position:absolute;left:127px;top:350px;font-size:18px}
.socials{position:absolute;left:196px;top:370px;display:flex;gap:6px}
.socials i{width:12px;height:12px;border-radius:50%;border:1.5px solid #fff;display:block}
.fcol{position:absolute;top:324px;font-family:var(--head);font-size:8px;color:#fff;line-height:11.5px}
.fcol h5{font-weight:500;font-size:8.5px;color:#dfe6f0;margin-bottom:6px;letter-spacing:.5px}
.legal{position:absolute;top:418px;font-family:var(--head);font-size:7.5px;color:#fff}
.tagline{position:absolute;top:450px;left:0;width:1200px;text-align:center;font-family:var(--head);font-weight:700;font-size:32.5px;color:rgba(255,255,255,.3);letter-spacing:2px;white-space:nowrap}
</style>
</head>
<body>

<!-- HERO -->
<section class="sec hero">
  <div class="hero-photo" role="img" aria-label="Blue sports coupe in front of snowy mountains"></div>
  <nav class="nav">
    <div class="logo">MotorLane</div>
    <div class="nav-links"><span>Search</span><span>Sell Your Car</span><span>Deals</span><span>Insurance</span><span>Research</span></div>
    <span class="nav-btn" style="left:760px;background:var(--blue);color:#fff">Login</span>
    <span class="nav-btn" style="left:866px;background:#fff;color:#333">Sign up</span>
  </nav>
  <h1>Find Your <strong>Next Car</strong><br>Without Searching<br>Thousands of Listings</h1>
  <p class="hero-lead">Describe your car once. Let dealers compete for your business.</p>
  <span class="btn btn-solid" style="left:117px;top:253px;width:170px;height:24px">Start Searching
    <svg width="14" height="14" viewBox="0 0 14 14" fill="none" stroke="#fff" stroke-width="1.5"><circle cx="6" cy="6" r="4.5"/><path d="M9.5 9.5 13 13"/></svg></span>
  <span class="btn btn-ghost" style="left:294px;top:253px;width:167px;height:24px">Watch How It works</span>
  <div class="stats">
    <div class="stat" style="left:203px"><b>10,000+</b>Buyers</div>
    <div class="stat" style="left:478px"><b>500+</b>Verified Dealers</div>
    <div class="stat" style="left:777px"><b>95%</b>Match Accuracy</div>
  </div>
</section>

<!-- FIND MY CAR -->
<section class="sec find">
  <div class="find-photo" role="img" aria-label="Blue crossover SUV, front three-quarter view"></div>
  <h2>Find My Car</h2>
  <div class="select" style="left:497px;width:170px">Choose Make<svg width="9" height="6"><path d="M1 1l3.5 3.5L8 1" stroke="#333" fill="none"/></svg></div>
  <div class="select" style="left:680px;width:170px">Choose Model<svg width="9" height="6"><path d="M1 1l3.5 3.5L8 1" stroke="#333" fill="none"/></svg></div>
  <div class="select" style="left:865px;width:173px">Budget<svg width="9" height="6"><path d="M1 1l3.5 3.5L8 1" stroke="#333" fill="none"/></svg></div>
  <p class="find-quote">"Looking for AWD SUV under 35k"</p>
  <div class="find-go">Search Inventory
    <svg width="16" height="16" viewBox="0 0 16 16" fill="none" stroke="#111" stroke-width="1.6"><circle cx="7" cy="7" r="5"/><path d="M11 11l4 4"/></svg></div>
</section>

<!-- HOW IT WORKS -->
<section class="sec how">
  <h2 class="h-title abs" style="top:46px">How MotorLane Works</h2>
  <p class="h-sub abs" style="top:89px">Tell us once, get matched with dealers automatically fast.</p>

  <div class="step" style="left:131px">
    <svg class="abs" style="left:34px;top:0" width="40" height="34" viewBox="0 0 40 34" fill="none" stroke="#0b7bff" stroke-width="1.5"><rect x="2" y="14" width="26" height="10" rx="3"/><circle cx="8" cy="26" r="3"/><circle cx="22" cy="26" r="3"/><circle cx="28" cy="11" r="8"/><path d="M34 17l5 5"/></svg>
    <span class="step-num" style="left:156px">1</span>
    <h3>Find Your Car</h3>
    <p>Search our inventory for the make, model, and year you want.</p>
  </div>
  <svg class="step-div" style="left:328px" viewBox="0 0 24 106" fill="none" stroke="#555"><path d="M1 0v106M1 40l20 13-20 13"/></svg>

  <div class="step" style="left:376px">
    <svg class="abs" style="left:30px;top:-4px" width="48" height="40" viewBox="0 0 48 40" fill="none" stroke="#0b7bff" stroke-width="1.5"><rect x="16" y="12" width="16" height="16" rx="2"/><path d="M20 12V6M28 12V6M20 34v-6M28 34v-6M16 16h-6M16 24h-6M32 16h6M32 24h6"/><circle cx="8" cy="6" r="3"/><circle cx="40" cy="6" r="3"/><circle cx="40" cy="34" r="3"/></svg>
    <span class="step-num" style="left:150px">2</span>
    <h3>Start MotorLane AI<br>Negotiations</h3>
    <p>MotorLane makes dealers compete for you.</p>
  </div>
  <svg class="step-div" style="left:578px" viewBox="0 0 24 106" fill="none" stroke="#555"><path d="M1 0v106M1 40l20 13-20 13"/></svg>

  <div class="step" style="left:620px">
    <svg class="abs" style="left:44px;top:0" width="40" height="36" viewBox="0 0 40 36" fill="none" stroke="#0b7bff" stroke-width="1.5"><rect x="2" y="2" width="36" height="11" rx="2"/><path d="M9 5l1 2h2l-1.5 1.5.5 2-2-1-2 1 .5-2L6 7h2zM20 5l1 2h2l-1.5 1.5.5 2-2-1-2 1 .5-2L17 7h2zM31 5l1 2h2l-1.5 1.5.5 2-2-1-2 1 .5-2L28 7h2z"/><rect x="2" y="18" width="8" height="6" rx="1"/><rect x="2" y="28" width="8" height="6" rx="1"/><path d="M14 21h24M14 31h24"/></svg>
    <span class="step-num" style="left:170px">3</span>
    <h3>Review Your Offers</h3>
    <p>Watch competing offers come in from multiple dealers.</p>
  </div>
  <svg class="step-div" style="left:826px" viewBox="0 0 24 106" fill="none" stroke="#555"><path d="M1 0v106M1 40l20 13-20 13"/></svg>

  <div class="step" style="left:866px">
    <svg class="abs" style="left:38px;top:-2px" width="42" height="38" viewBox="0 0 42 38" fill="none" stroke="#0b7bff" stroke-width="1.5"><rect x="10" y="2" width="22" height="26" rx="2"/><path d="M15 10l2 2 4-4M15 18h12M15 23h8"/><path d="M2 26l8 4 6-3 6 4 6-3M40 26l-6 4"/></svg>
    <span class="step-num" style="left:168px">4</span>
    <h3>Choose Your Deal</h3>
    <p>Pick the winning offer and drive it home.</p>
  </div>

  <span class="btn btn-line" style="left:512px;top:283px;width:191px;height:24px">Watch Dealers Compete</span>
</section>

<!-- DAILY DEALS -->
<section class="sec deals" role="img" aria-label="Blue sky over a grassy field with a white SUV parked below">
  <h2 class="h-title abs" style="top:18px;letter-spacing:2px">Daily Deals</h2>
  <p class="h-sub abs" style="top:56px">Technology Finds New Deals So You Never Miss Savings</p>

  <span class="round" style="left:68px;top:200px"><svg width="8" height="10"><path d="M6 1L2 5l4 4" stroke="#333" fill="none" stroke-width="1.4"/></svg></span>
  <span class="round" style="left:1102px;top:200px"><svg width="8" height="10"><path d="M2 1l4 4-4 4" stroke="#333" fill="none" stroke-width="1.4"/></svg></span>

  <article class="deal" style="left:116px;width:231px">
    <div class="deal-photo" role="img" aria-label="Black compact SUV"></div>
    <span class="heart"><svg width="11" height="10" viewBox="0 0 11 10"><path d="M5.5 9L1.3 5A2.3 2.3 0 015.5 2a2.3 2.3 0 014.2 3z" fill="none" stroke="#fff" stroke-width="1.1"/></svg></span>
    <h4>Used 2024 Corvan<br>Trailstar</h4>
    <span class="price">$23,018</span>
    <span class="miles"><svg width="9" height="9"><circle cx="4.5" cy="4.5" r="3.8" fill="none" stroke="#333"/></svg>16,134 mi</span>
    <span class="est">Est.$341/mo*</span>
    <span class="dom">54 days on market</span>
    <span class="color"><i></i>Black</span>
    <span class="loc"><svg width="8" height="10"><path d="M4 9S1 5.5 1 3.8a3 3 0 016 0C7 5.5 4 9 4 9z" fill="none" stroke="#0b7bff"/></svg>San Antonio, TX</span>
  </article>

  <article class="deal" style="left:362px;width:217px">
    <div class="deal-photo" role="img" aria-label="Black electric luxury sedan"></div>
    <span class="heart"><svg width="11" height="10" viewBox="0 0 11 10"><path d="M5.5 9L1.3 5A2.3 2.3 0 015.5 2a2.3 2.3 0 014.2 3z" fill="none" stroke="#fff" stroke-width="1.1"/></svg></span>
    <h4>2023 Veltra<br>EQ7</h4>
    <span class="price">$61,999</span>
    <span class="miles"><svg width="9" height="9"><circle cx="4.5" cy="4.5" r="3.8" fill="none" stroke="#333"/></svg>29,118 mi</span>
    <span class="est">Est.$341/mo*</span>
    <span class="dom">54 days on market</span>
    <span class="color"><i></i>Black</span>
    <span class="loc"><svg width="8" height="10"><path d="M4 9S1 5.5 1 3.8a3 3 0 016 0C7 5.5 4 9 4 9z" fill="none" stroke="#0b7bff"/></svg>San Antonio, TX</span>
  </article>

  <article class="deal" style="left:608px;width:230px">
    <div class="deal-photo" role="img" aria-label="Black electric hatchback"></div>
    <span class="heart"><svg width="11" height="10" viewBox="0 0 11 10"><path d="M5.5 9L1.3 5A2.3 2.3 0 015.5 2a2.3 2.3 0 014.2 3z" fill="none" stroke="#fff" stroke-width="1.1"/></svg></span>
    <h4>2023 Hanra Volt 5</h4>
    <span class="price">$27,883</span>
    <span class="miles"><svg width="9" height="9"><circle cx="4.5" cy="4.5" r="3.8" fill="none" stroke="#333"/></svg>44,291 mi</span>
    <span class="est">Est.$341/mo*</span>
    <span class="dom">54 days on market</span>
    <span class="color"><i></i>Black</span>
    <span class="loc"><svg width="8" height="10"><path d="M4 9S1 5.5 1 3.8a3 3 0 016 0C7 5.5 4 9 4 9z" fill="none" stroke="#0b7bff"/></svg>Roseville, CA (7,503 mi away)</span>
  </article>

  <article class="deal" style="left:853px;width:228px">
    <div class="deal-photo" role="img" aria-label="Black minivan"></div>
    <span class="heart"><svg width="11" height="10" viewBox="0 0 11 10"><path d="M5.5 9L1.3 5A2.3 2.3 0 015.5 2a2.3 2.3 0 014.2 3z" fill="none" stroke="#fff" stroke-width="1.1"/></svg></span>
    <h4>2017 Calder<br>Voyage</h4>
    <span class="price">$12,889</span>
    <span class="miles"><svg width="9" height="9"><circle cx="4.5" cy="4.5" r="3.8" fill="none" stroke="#333"/></svg>16,134 mi</span>
    <span class="est">Est.$341/mo*</span>
    <span class="dom">54 days on market</span>
    <span class="color"><i></i>Black</span>
    <span class="loc"><svg width="8" height="10"><path d="M4 9S1 5.5 1 3.8a3 3 0 016 0C7 5.5 4 9 4 9z" fill="none" stroke="#0b7bff"/></svg>East Hartford, CT (7,065 mi away)</span>
  </article>

  <span class="abs" style="left:0;width:1227px;text-align:center;top:336px;font-family:var(--head);font-size:10px;color:#0b64d8">View All Deals</span>
  <div class="deals-car" role="img" aria-label="White SUV on grass"></div>
</section>

<!-- OLD WAY VS NEW WAY + INTELLIGENCE -->
<section class="sec compare">
  <h2 class="h-title abs" style="top:14px;color:#222;letter-spacing:2px">The Old Way vs The MotorLane Way</h2>
  <div class="col-old">
    <h3>The Old Way</h3>
    <ul>
      <li>You visit dealership after dealership</li>
      <li>Every salesperson has an agenda</li>
      <li>Inconsistent pricing and hidden fees</li>
      <li>Hours of back-and-forth negotiation</li>
      <li>You leave wondering if you got played</li>
      <li>Pressure to decide on dealer's timeline</li>
    </ul>
  </div>
  <div class="col-new">
    <h3>The MotorLane Way</h3>
    <ul>
      <li>Dealers come to you</li>
      <li>MotorLane works for buyers, not dealers</li>
      <li>Transparent pricing from competing dealers</li>
      <li>Built-in negotiation handles it</li>
      <li>You leave knowing you got the best deal</li>
      <li>Your timeline. Your decision</li>
    </ul>
  </div>
  <div class="compare-car" role="img" aria-label="Blue crossover SUV"></div>

  <h2 class="powered">Powered By Intelligent<br>Vehicle Matching</h2>

  <div class="dash">
    <aside class="side">
      <div class="brand"><i></i>MotorLane</div>
      <ul>
        <li class="on"><i></i>Overview</li>
        <li><i></i>My Search</li>
        <li><i></i>Matches</li>
        <li><i></i>Offers<span class="badge">4</span></li>
        <li><i></i>Messages</li>
        <li><i></i>Saved Cars</li>
        <li><i></i>Market Insights</li>
        <li><i></i>Account</li>
        <li><i></i>Settings</li>
      </ul>
      <div class="help"><b>Need Help?</b>Chat with our experts<span>Start Chat</span></div>
    </aside>

    <div class="dash-head"><b>AI-Powered Vehicle Matching</b><p>Real-time intelligence. Smarter car buying.</p></div>
    <div class="pill" style="left:617px;width:142px"><span style="color:var(--green)">●</span> Live Market Data<br><span style="color:#8794b3;font-size:6px">Updated just now</span></div>
    <div class="pill" style="left:786px;width:210px;line-height:13px">My Search: 2022+ SUV</div>

    <div class="card" style="left:164px;width:185px">
      <div class="lbl">MATCHING SCORE</div>
      <svg class="abs" style="left:47px;top:20px" width="90" height="70" viewBox="0 0 90 70"><path d="M10 62A38 38 0 1180 62" fill="none" stroke="#1a2a50" stroke-width="6"/><path d="M10 62A38 38 0 1180 62" fill="none" stroke="#1e7bff" stroke-width="6" stroke-dasharray="150 200"/></svg>
      <div class="big abs" style="left:0;right:0;top:44px;text-align:center;font-size:22px">94<small style="font-size:12px">%</small></div>
      <div class="note" style="top:72px;color:var(--green)">Excellent Match</div>
      <div class="note" style="top:94px"><span style="color:var(--green)">↑ +12%</span> above average</div>
      <div class="note" style="top:106px">Your search is highly matched<br>with available inventory</div>
    </div>

    <div class="card" style="left:362px;width:194px">
      <div class="lbl">INVENTORY MATCH %</div>
      <div class="big abs" style="left:24px;top:26px;font-size:26px;color:var(--green)">82<small style="font-size:14px">%</small></div>
      <div class="abs" style="left:24px;top:62px;font-size:7px">245 Matching Vehicles</div>
      <svg class="abs" style="left:24px;top:74px" width="110" height="8"><g fill="#27d17f"><rect x="0" width="5" height="8"/><rect x="7" width="5" height="8"/><rect x="14" width="5" height="8"/><rect x="21" width="5" height="8"/><rect x="28" width="5" height="8"/><rect x="35" width="5" height="8"/><rect x="42" width="5" height="8"/><rect x="49" width="5" height="8"/><rect x="56" width="5" height="8"/><rect x="63" width="5" height="8"/><rect x="70" width="5" height="8"/></g><g fill="#24365e"><rect x="77" width="5" height="8"/><rect x="84" width="5" height="8"/><rect x="91" width="5" height="8"/></g></svg>
      <div class="abs" style="left:20px;top:90px;width:150px;height:22px;background:#14203e;border-radius:3px;font-size:6.5px;padding:3px 0 0 18px">Live Inventory<br><span style="color:#8794b3">Updated just now</span></div>
      <div class="link"><span>View matching vehicles</span><span>›</span></div>
    </div>

    <div class="card" style="left:569px;width:194px">
      <div class="lbl">PRICE CONFIDENCE</div>
      <svg class="abs" style="left:42px;top:16px" width="110" height="60" viewBox="0 0 110 60"><path d="M10 55A45 45 0 01100 55" fill="none" stroke="#1a2a50" stroke-width="7"/><path d="M10 55A45 45 0 01100 55" fill="none" stroke="#8e4dff" stroke-width="7" stroke-dasharray="125 200"/></svg>
      <div class="abs" style="left:0;right:0;top:42px;text-align:center;font-size:10px;font-weight:700;color:#b47dff">HIGH</div>
      <div class="big abs" style="left:0;right:0;top:54px;text-align:center;font-size:18px">89<small style="font-size:10px">%</small></div>
      <svg class="abs" style="left:22px;top:82px" width="150" height="18"><path d="M0 15l15-3 15 2 15-5 15 3 15-6 15 2 15-5 15 1 15-4 15-2" fill="none" stroke="#8e4dff" stroke-width="1.2"/></svg>
      <div class="note" style="top:104px">Prices are optimal right now<br>Based on market trends &amp; history</div>
      <div class="link"><span>View price analysis</span><span>›</span></div>
    </div>

    <div class="card" style="left:776px;width:221px">
      <div class="lbl">DEALER RESPONSE TIME</div>
      <svg class="abs" style="left:30px;top:22px" width="44" height="44"><circle cx="22" cy="22" r="18" fill="none" stroke="#1a2a50" stroke-width="4"/><circle cx="22" cy="22" r="18" fill="none" stroke="#27d17f" stroke-width="4" stroke-dasharray="80 200" transform="rotate(-90 22 22)"/></svg>
      <div class="big abs" style="left:76px;top:28px;font-size:20px">2.3<small style="font-size:12px">h</small></div>
      <div class="abs" style="left:74px;top:52px;font-size:7px">Average Response</div>
      <div class="abs" style="left:40px;top:70px;width:140px;height:12px;border-radius:6px;background:#123328;color:var(--green);font-size:6.5px;text-align:center;line-height:12px;font-weight:700">Fast Response</div>
      <div class="note" style="top:90px">97% of dealers respond<br>within 6 hours</div>
      <div class="link"><span>View dealer activity</span><span>›</span></div>
    </div>

    <div class="insights">
      <div class="lbl" style="left:14px;top:8px">MARKET INSIGHTS</div>
      <div class="abs" style="left:14px;top:18px;font-size:6px;color:#8794b3">Key trends and insights to help you make the best decision</div>
      <div class="tabs"><span>7D</span><span class="on">30D</span><span>90D</span><span>1Y</span></div>

      <div class="ins-col" style="left:14px;width:200px;padding-right:10px">
        <div class="lbl" style="left:0;top:0">VEHICLE DEMAND</div>
        <div class="abs" style="right:12px;top:0;font-size:6px;color:#8794b3">vs last 30 days</div>
        <div style="position:absolute;top:12px;left:0;width:190px">
          <div class="row"><span style="width:50px">SUVs</span><span class="bar" style="width:80px;background:#1e7bff"></span><span style="margin-left:auto">High</span></div>
          <div class="row"><span style="width:50px">Trucks</span><span class="bar" style="width:70px;background:#1e7bff"></span><span style="margin-left:auto">High</span></div>
          <div class="row"><span style="width:50px">Sedans</span><span class="bar" style="width:52px;background:#8e4dff"></span><span style="margin-left:auto">Medium</span></div>
          <div class="row"><span style="width:50px">EVs</span><span class="bar" style="width:76px;background:#27d17f"></span><span style="margin-left:auto">Rising</span></div>
          <div class="row"><span style="width:50px">Luxury</span><span class="bar" style="width:48px;background:#8e4dff"></span><span style="margin-left:auto">Medium</span></div>
        </div>
        <div class="ins-link" style="left:0">View full report</div>
      </div>

      <div class="ins-col" style="left:222px;width:170px;padding-left:6px">
        <div class="lbl" style="left:6px;top:0">PRICE TREND</div>
        <div class="abs" style="right:12px;top:0;font-size:6px;color:#8794b3">vs last 30 days</div>
        <div class="big abs" style="left:6px;top:10px;font-size:14px;color:var(--green)">-2.4%</div>
        <div class="abs" style="left:6px;top:28px;font-size:6px;color:#8794b3">Average Price Change</div>
        <svg class="abs" style="left:6px;top:38px" width="150" height="54"><path d="M10 14l12 8 12-2 12 10 12-4 12 12 12-6 12 14 12-8 12 10 12-4 12 12V54H10z" fill="#1a5a3a" opacity=".6"/><path d="M10 14l12 8 12-2 12 10 12-4 12 12 12-6 12 14 12-8 12 10 12-4 12 12" fill="none" stroke="#27d17f" stroke-width="1.2"/></svg>
        <div class="abs" style="left:20px;top:94px;font-size:5px;color:#8794b3;word-spacing:14px">Apr 24 May 1 May 8 May 15 May 22</div>
        <div class="ins-link" style="left:6px">View pricing trends</div>
      </div>

      <div class="ins-col" style="left:400px;width:170px">
        <div class="lbl" style="left:8px;top:0">MARKET CONDITIONS</div>
        <div class="abs" style="left:0;right:0;top:14px;text-align:center;font-size:12px;font-weight:700;color:var(--green)">Favorable</div>
        <div class="abs" style="left:0;right:0;top:29px;text-align:center;font-size:6px;color:#aebadb">Buying Window</div>
        <svg class="abs" style="left:45px;top:42px" width="80" height="36"><path d="M6 34A34 34 0 0174 34" fill="none" stroke="#1a2a50" stroke-width="5"/><path d="M6 34A34 34 0 0174 34" fill="none" stroke="#ffb020" stroke-width="5" stroke-dasharray="30 200"/><path d="M6 34A34 34 0 0174 34" fill="none" stroke="#27d17f" stroke-width="5" stroke-dasharray="0 30 60 200"/></svg>
        <div class="abs" style="left:0;right:0;top:80px;text-align:center;font-size:6.5px;font-weight:700;color:#fff">Great time to buy!</div>
        <div class="abs" style="left:0;right:0;top:90px;text-align:center;font-size:5.5px;color:#aebadb">Prices are below average and<br>inventory is increasing</div>
        <div class="ins-link" style="left:8px">View market outlook</div>
      </div>

      <div class="ins-col" style="left:580px;width:240px;border:none">
        <div class="lbl" style="left:8px;top:0">POPULAR SEARCHES</div>
        <div class="abs" style="right:0;top:0;font-size:6px;color:#8794b3">vs last 30 days</div>
        <div style="position:absolute;top:12px;left:8px;width:230px">
          <div class="row"><span style="width:14px">1</span><span style="width:90px">3 Row SUV</span><svg width="50" height="8"><path d="M0 6l8-3 8 2 8-4 8 3 8-2 10-1" fill="none" stroke="#4f9bff"/></svg><span style="margin-left:auto;color:var(--green)">+ 28%</span></div>
          <div class="row"><span style="width:14px">2</span><span style="width:90px">Hybrid SUV</span><svg width="50" height="8"><path d="M0 6l8-3 8 2 8-4 8 3 8-2 10-1" fill="none" stroke="#4f9bff"/></svg><span style="margin-left:auto;color:var(--green)">+ 22%</span></div>
          <div class="row"><span style="width:14px">3</span><span style="width:90px">Electric SUV</span><svg width="50" height="8"><path d="M0 6l8-3 8 2 8-4 8 3 8-2 10-1" fill="none" stroke="#4f9bff"/></svg><span style="margin-left:auto;color:var(--green)">+ 18%</span></div>
          <div class="row"><span style="width:14px">4</span><span style="width:90px">Off Road SUV</span><svg width="50" height="8"><path d="M0 6l8-3 8 2 8-4 8 3 8-2 10-1" fill="none" stroke="#4f9bff"/></svg><span style="margin-left:auto;color:var(--green)">+ 15%</span></div>
          <div class="row"><span style="width:14px">5</span><span style="width:90px">Luxury SUV</span><svg width="50" height="8"><path d="M0 6l8-3 8 2 8-4 8 3 8-2 10-1" fill="none" stroke="#4f9bff"/></svg><span style="margin-left:auto;color:var(--green)">+ 12%</span></div>
        </div>
        <div class="ins-link" style="left:8px">View all trends</div>
      </div>
    </div>

    <div class="dash-foot">
      <svg class="abs" style="left:22px;top:7px" width="20" height="20"><circle cx="10" cy="10" r="8" fill="none" stroke="#1e7bff" stroke-width="2" stroke-dasharray="36 50"/></svg>
      <div class="abs" style="left:74px;top:6px"><b style="color:#fff">We're finding you the best matches!</b><br><span style="font-size:6px">Our AI is scanning 500+ dealers and updating results in real-time.</span></div>
      <div class="abs" style="left:420px;top:6px"><b style="color:#fff;font-size:9px">500+</b><br><span style="font-size:6px">Active Dealers</span></div>
      <div class="abs" style="left:560px;top:6px"><b style="color:#fff;font-size:9px">12,845</b><br><span style="font-size:6px">Vehicles Scanned</span></div>
      <div class="abs" style="left:700px;top:6px"><b style="color:#fff;font-size:9px">98%</b><br><span style="font-size:6px">Match Accuracy</span></div>
    </div>
  </div>
</section>

<!-- POPULAR SEARCHES -->
<section class="sec popular">
  <h2 class="h-title abs" style="top:24px;letter-spacing:2px">Popular Searches</h2>
  <p class="h-sub abs" style="top:62px">Trending Vehicle Searches Powered By Real-Time Market Data</p>
  <div class="tile" style="left:116px"><div class="ph" role="img" aria-label="SUV"></div><span>SUVs</span></div>
  <div class="tile" style="left:281px"><div class="ph" role="img" aria-label="Electric car"></div><span>Electric</span></div>
  <div class="tile" style="left:445px"><div class="ph" role="img" aria-label="Luxury sedan" style="background:linear-gradient(180deg,#f0f2f5,#a9b0bb)"></div><span>Luxury</span></div>
  <div class="tile" style="left:609px"><div class="ph" role="img" aria-label="Hybrid hatchback" style="background:linear-gradient(180deg,#3a6cd8,#1a3478)"></div><span>Hybrid</span></div>
  <div class="tile" style="left:773px"><div class="ph" role="img" aria-label="Family SUV"></div><span>Family Cars</span></div>
  <div class="tile" style="left:937px"><div class="ph" role="img" aria-label="Sports car" style="background:linear-gradient(180deg,#3fb0e0,#156a95)"></div><span>Sports Cars</span></div>
</section>

<!-- TESTIMONIALS -->
<section class="sec reviews">
  <h2 class="h-title abs" style="top:20px;letter-spacing:2px">Buyers Are Finding Cars Faster</h2>
  <p class="h-sub abs" style="top:61px">Real Buyers. Real Matches. Faster Car Buying Experiences.</p>
  <span class="arrow-c" style="left:110px;top:117px"><svg width="8" height="10"><path d="M6 1L2 5l4 4" stroke="#333" fill="none" stroke-width="1.4"/></svg></span>
  <span class="arrow-c" style="left:1085px;top:117px"><svg width="8" height="10"><path d="M2 1l4 4-4 4" stroke="#333" fill="none" stroke-width="1.4"/></svg></span>
  <div class="review" style="left:162px"><div class="stars">★★★★★</div><q>Received 4 offers within 48 hours</q><cite>— Marcus</cite></div>
  <div class="review" style="left:463px"><div class="stars">★★★★★</div><q>Finally stopped wasting weekends</q><cite>— Sophie</cite></div>
  <div class="review" style="left:764px"><div class="stars">★★★★★</div><q>Much easier than dealership hopping</q><cite>— Daniel</cite></div>
  <span class="btn btn-line" style="left:512px;top:190px;width:191px;height:24px">View all Testimonials</span>
</section>

<!-- FAQ -->
<section class="sec faq">
  <div class="faq-word" aria-hidden="true">Questions</div>
  <h2>You Have Questions,<br>We Have Answers</h2>
  <div class="faq-photo" role="img" aria-label="Blue SUV, front three-quarter view"></div>
  <div class="q" style="top:120px">Does MotorLane cost anything to use?<i>+</i></div>
  <div class="q" style="top:162px">Do I still have to negotiate with dealerships?<i>+</i></div>
  <div class="q" style="top:202px">How do I know the price is fair?<i>+</i></div>
  <div class="q" style="top:244px">How does AI matching work for dealers?<i>+</i></div>
  <span class="abs" style="left:540px;top:282px;font-family:var(--head);font-size:10px;color:var(--blue);text-decoration:underline">View all Faq's</span>
</section>

<!-- CTA + FOOTER -->
<section class="sec cta" role="img" aria-label="Grey SUV on an open road with mountains behind">
  <h2>Stop Searching. Start Matching.</h2>
  <p>Tell us what you want once.<br>Receive offers from dealers that already have it.</p>
  <span class="btn btn-solid" style="left:396px;top:142px;width:168px;height:24px">Start Searching
    <svg width="14" height="14" viewBox="0 0 14 14" fill="none" stroke="#fff" stroke-width="1.5"><circle cx="6" cy="6" r="4.5"/><path d="M9.5 9.5 13 13"/></svg></span>
  <span class="btn" style="left:575px;top:142px;width:171px;height:24px;background:#fff;color:#333">Chat With AI
    <svg width="22" height="13" viewBox="0 0 22 13" fill="none" stroke="#333"><rect x="3" y="1.5" width="16" height="10" rx="2"/><circle cx="8" cy="6.5" r="1.3"/><circle cx="14" cy="6.5" r="1.3"/><path d="M1 5v3M21 5v3"/></svg></span>
  <div class="cta-car"></div>

  <div class="logo foot-logo">MotorLane</div>
  <div class="socials"><i></i><i></i></div>

  <div class="fcol" style="left:427px"><h5>FOR BUYERS</h5>Search<br>Daily Deals<br>How It Works<br>Car Value Calculator</div>
  <div class="fcol" style="left:590px"><h5>RESOURCES</h5>Guides<br>Research<br>FAQ</div>
  <div class="fcol" style="left:718px"><h5>COMPANY</h5>About Us<br>Contact<br>Affiliate Program</div>
  <div class="fcol" style="left:892px"><h5>CONTACT US</h5>
    <div style="display:flex;gap:12px;align-items:center;font-size:10px;margin-top:6px"><svg width="10" height="10" viewBox="0 0 10 10"><path d="M2 1l2 2-1 1.5a6 6 0 002.5 2.5L7 6l2 2-1.5 1.5C4 9 1 6 .5 2.5z" fill="#fff"/></svg>123 456-7890</div>
    <div style="display:flex;gap:12px;align-items:center;font-size:9.5px;margin-top:8px;text-decoration:underline"><svg width="11" height="8" viewBox="0 0 11 8"><rect x=".5" y=".5" width="10" height="7" fill="none" stroke="#fff"/><path d="M.5.5l5 4 5-4" fill="none" stroke="#fff"/></svg>hello@motorlane.net</div>
  </div>

  <div class="legal" style="left:118px">© 2026 MotorLane. All rights reserved.</div>
  <div class="legal" style="left:760px;word-spacing:2px">Report Problem &nbsp;|&nbsp; Terms &amp; Conditions &nbsp;|&nbsp; Privacy Policy</div>
  <div class="tagline">THE SMARTER WAY TO BUY YOUR NEXT CAR</div>
</section>

</body>
</html>
```